Building restoration company expanding services

We need a flyer to promote our new 'Commercial Cleaning" and 'Property Maintenance' Services to new and existing customers.
We want to use our current logo and colours and add our new catch phrase, 'Restore, Repair and Maintain' instead of 'building a healthy future' These 2 new services can be in new colours to flow with the 'air, fire, flood and mould' such as a yellow and purple perhaps.
We are offering a free 'Moisture Inspection' valued at $199 once a year. this will prevent any costly building repairs as a result of pipes leaking etc
Our website has more detailed information www.pelmarworkshops.net
We would like people to know we are trusted, professionals from working in the industry for over 16 years.
We are providing these extra services due to our current customers requests. Due to our background we can provide repairs or restoration to almost anything and by maintaining many costly replacements or repairs are avoided.

Target Market(s)

Corporate Businesses
Builders

Industry/Entity Type

It Company

Requirements
Must have
• Contact details
• Our colours
• Logo
Nice to have
• Images to reflect our professional and trusted company.

```html
<!DOCTYPE html>
<html lang="en">
<head>
<meta charset="utf-8">
<title>Pelmar flyers</title>
<link rel="stylesheet" href="https://fonts.googleapis.com/css2?family=Montserrat:wght@500;600;700&family=Roboto:wght@300;400;500;700&display=swap">
<style>
  :root {
    --bg: #9a9a9a;
    --paper: #f4f4f4;
    --grey: #636466;
    --grey-dark: #4e4f51;
    --green: #86c440;
    --green-dark: #4d7a2a;
    --yellow: #f6ec13;
    --purple: #a43f95;
    --red: #c0272d;
    --white: #ffffff;
  }
  * { box-sizing: border-box; margin: 0; padding: 0; }
  html, body { width: 1200px; height: 960px; overflow: hidden; background: var(--bg); }
  body { position: relative; font-family: 'Roboto', Arial, sans-serif; }

  .flyer {
    position: absolute;
    width: 615px; height: 875px;
    background: var(--paper);
    transform: scale(0.8);
    transform-origin: top left;
    overflow: hidden;
  }
  .flyer--front { left: 60px; top: 130px; }
  .flyer--back { left: 624px; top: 126px; }
  .flyer > svg.shapes { position: absolute; left: 0; top: 0; }
  .abs { position: absolute; }

  .photo-family { position: absolute; left: 0; top: 0; width: 615px; height: 363px;
    background: linear-gradient(135deg, #e7e2d6 0%, #d9b8a4 35%, #b9cf9a 70%, #eef2e8 100%); }
  .photo-plumber { position: absolute; left: 0; top: 0; width: 615px; height: 437px;
    background: linear-gradient(120deg, #e9ecef 0%, #d6dbe0 45%, #4a74b8 75%, #2c4f8c 100%);
    clip-path: polygon(150px 0, 615px 0, 615px 437px, 400px 437px, 265px 240px); }

  .brand-mark {
    position: absolute; width: 170px; height: 170px;
    background: var(--grey); border-radius: 26px;
    transform: rotate(45deg);
    box-shadow: 0 0 0 8px var(--paper);
  }
  .brand-name {
    position: absolute; width: 220px; text-align: center;
    font-family: 'Montserrat', Arial, sans-serif; font-weight: 700;
    font-size: 46px; color: var(--white); letter-spacing: 0.5px;
  }

  .experience {
    position: absolute; left: 413px; top: 222px; width: 180px; height: 180px;
    border-radius: 50%; background: var(--green); border: 5px solid var(--grey);
    color: var(--white); text-align: center; font-family: 'Roboto', Arial, sans-serif;
  }
  .experience__over { position: absolute; top: 18px; width: 100%; font-size: 19px; font-weight: 500; }
  .experience__num { position: absolute; top: 30px; left: 22px; font-size: 86px; font-weight: 700; letter-spacing: -4px; line-height: 1; }
  .experience__years { position: absolute; top: 84px; left: 113px; font-size: 22px; font-weight: 500; }
  .experience__label { position: absolute; top: 113px; width: 100%; font-size: 27px; font-weight: 500; }

  .offer-title { left: 20px; top: 452px; font-family: 'Roboto', Arial, sans-serif; font-weight: 700; font-size: 50px; line-height: 50px; }
  .offer-title .hl { color: var(--green); }
  .offer-title .dk { color: var(--grey-dark); }
  .offer-band { left: 0; top: 557px; width: 287px; height: 35px; background: var(--green);
    color: var(--white); font-size: 20px; line-height: 35px; padding-left: 16px; font-weight: 300; }
  .offer-band b { color: var(--grey-dark); font-weight: 500; }

  .mission-title { right: 10px; top: 480px; font-family: 'Montserrat', Arial, sans-serif; font-weight: 700; font-size: 34px; color: var(--white); }
  .mission-text { right: 12px; top: 533px; text-align: right; color: var(--white); font-size: 16px; line-height: 21px; font-weight: 300; white-space: nowrap; }
  .specialists { right: 17px; top: 657px; text-align: right; color: var(--white); font-size: 18px; line-height: 25px; font-weight: 300; white-space: nowrap; }
  .specialists b { font-weight: 500; }

  .seal { left: 38px; top: 677px; width: 130px; height: 130px; border-radius: 50%;
    border: 7px solid var(--red); }

  .contact-call { font-family: 'Montserrat', Arial, sans-serif; font-weight: 600; color: var(--white); white-space: nowrap; }
  .phone { display: flex; align-items: center; gap: 10px; font-family: 'Montserrat', Arial, sans-serif; font-weight: 700; color: var(--white); white-space: nowrap; }
  .phone svg { flex: none; }
  .web { font-family: 'Montserrat', Arial, sans-serif; font-weight: 600; color: var(--white); font-size: 18px; white-space: nowrap; }
  .web span { color: var(--green); }

  .intro-green { left: 10px; top: 200px; color: var(--grey-dark); font-size: 17.5px; line-height: 24px; font-weight: 400; }
  .intro-green b { color: var(--white); font-weight: 700; }

  .service-title { left: 28px; top: 475px; font-family: 'Montserrat', Arial, sans-serif; font-weight: 700; font-size: 31px; color: var(--green); }
  .service-list { left: 22px; top: 527px; list-style: none; color: var(--white); font-size: 15px; font-weight: 400; }
  .service-list li { display: flex; align-items: center; gap: 12px; height: 26.8px; }

  .tag { position: absolute; height: 47px; display: flex; align-items: center; justify-content: flex-end;
    padding-right: 22px; font-family: 'Montserrat', Arial, sans-serif; font-weight: 700; font-size: 30px;
    clip-path: polygon(0 0, 96% 0, 100% 100%, 0 100%); border-radius: 0 8px 8px 0; }
  .tag--restore { left: 305px; top: 522px; width: 182px; color: var(--white);
    background: linear-gradient(90deg, rgba(164,63,149,0) 0%, var(--purple) 30%); }
  .tag--repair { left: 345px; top: 578px; width: 198px; color: var(--grey-dark);
    background: linear-gradient(90deg, rgba(246,236,19,0) 0%, var(--yellow) 30%); }
  .tag--maintain { left: 395px; top: 639px; width: 198px; color: var(--white);
    background: linear-gradient(90deg, rgba(164,63,149,0) 0%, var(--purple) 30%); }

  .divider { left: 268px; top: 767px; width: 1px; height: 95px; background: var(--green); }
  .details { left: 284px; top: 778px; color: var(--white); font-size: 13px; line-height: 18px; }
  .details .row { display: flex; gap: 12px; align-items: flex-start; margin-bottom: 4px; }
  .details .row svg { flex: none; margin-top: 3px; }
</style>
</head>
<body>

<section class="flyer flyer--front">
  <div class="photo-family" role="img" aria-label="Photo of a smiling family of four outdoors"></div>
  <svg class="shapes" width="615" height="875" viewBox="0 0 615 875" aria-hidden="true">
    <polygon points="615,0 615,340 380,292" fill="#86c440"/>
    <polygon points="615,0 380,292 455,292" fill="#4d7a2a"/>
    <polygon points="0,363 615,363 615,440 0,440" fill="#f4f4f4"/>
    <polygon points="615,0 615,363 520,363" fill="#86c440"/>
    <polygon points="405,440 615,440 615,875 0,875" fill="#86c440"/>
    <polygon points="415,452 615,452 615,875 18,875" fill="#636466"/>
  </svg>
  <div class="experience">
    <div class="experience__over">OVER</div>
    <div class="experience__num">16</div>
    <div class="experience__years">years</div>
    <div class="experience__label">Experience</div>
  </div>
  <div class="brand-mark" style="left:221px; top:312px;"></div>
  <div class="brand-name" style="left:196px; top:368px;">pelmar</div>

  <div class="abs offer-title"><span class="hl">Moisture</span><br><span class="dk">Inspection</span></div>
  <div class="abs offer-band">valued at <b>$199</b> once a year.</div>

  <div class="abs mission-title">Our Mission</div>
  <p class="abs mission-text">Customer satisfaction and welfare<br>during what can be a very emotional<br>time is very important to us. We use our<br>expertise and knowledge to address the<br>situation in a highly professional manner.</p>
  <p class="abs specialists">Specialists in <b>Structual Drying,<br>Sub Floor Ventilation and Odour Elimination.</b></p>

  <div class="abs seal" role="img" aria-label="Trust seal"></div>

  <div class="abs contact-call" style="left:198px; top:734px; font-size:22px;">Send a Message or Call our Office</div>
  <div class="abs phone" style="left:246px; top:768px; font-size:36px;">
    <svg width="36" height="36" viewBox="0 0 36 36"><circle cx="18" cy="18" r="16" fill="none" stroke="#86c440" stroke-width="2.5"/><path d="M12 9c1-1 2-1 3 0l2 3c.6 1 .3 2-.5 2.6l-1 .8c1 2.2 2.8 4 5 5l.8-1c.6-.8 1.6-1.1 2.6-.5l3 2c1 1 1 2 0 3l-1.5 1.5c-5 1-14-8-13-13z" fill="#86c440"/></svg>
    0249 55 0183
  </div>
  <div class="abs web" style="left:198px; top:836px;">www.<span>pelmarworkshops</span>.net</div>
</section>

<section class="flyer flyer--back">
  <div class="photo-plumber" role="img" aria-label="Photo of a plumber fixing pipes under a sink"></div>
  <svg class="shapes" width="615" height="875" viewBox="0 0 615 875" aria-hidden="true">
    <polygon points="0,0 230,262 160,335 0,335" fill="#86c440"/>
    <polygon points="0,0 268,240 230,262" fill="#4d7a2a"/>
    <polygon points="0,437 615,437 615,875 0,875" fill="#f4f4f4"/>
    <polygon points="0,440 208,440 615,868 615,875 0,875" fill="#86c440"/>
    <polygon points="0,452 203,452 603,875 0,875" fill="#636466"/>
  </svg>
  <p class="abs intro-green">Specialists in<br><b>Structural Drying,<br>Sub Floor Ventilation<br>and Odour Elimination.</b></p>

  <div class="brand-mark" style="left:225px; top:312px;"></div>
  <div class="brand-name" style="left:200px; top:368px;">pelmar</div>

  <div class="abs service-title">Our Service</div>
  <ul class="abs service-list">
    <li><svg width="18" height="18" viewBox="0 0 18 18"><circle cx="9" cy="9" r="7.5" fill="none" stroke="#86c440" stroke-width="2"/><path d="M5.5 9.2l2.3 2.3 4.7-4.7" fill="none" stroke="#86c440" stroke-width="2"/></svg>Mould Remediation</li>
    <li><svg width="18" height="18" viewBox="0 0 18 18"><circle cx="9" cy="9" r="7.5" fill="none" stroke="#86c440" stroke-width="2"/><path d="M5.5 9.2l2.3 2.3 4.7-4.7" fill="none" stroke="#86c440" stroke-width="2"/></svg>Fire &amp; Smoke Damage</li>
    <li><svg width="18" height="18" viewBox="0 0 18 18"><circle cx="9" cy="9" r="7.5" fill="none" stroke="#86c440" stroke-width="2"/><path d="M5.5 9.2l2.3 2.3 4.7-4.7" fill="none" stroke="#86c440" stroke-width="2"/></svg>Odour Elimination</li>
    <li><svg width="18" height="18" viewBox="0 0 18 18"><circle cx="9" cy="9" r="7.5" fill="none" stroke="#86c440" stroke-width="2"/><path d="M5.5 9.2l2.3 2.3 4.7-4.7" fill="none" stroke="#86c440" stroke-width="2"/></svg>Water Damage</li>
    <li><svg width="18" height="18" viewBox="0 0 18 18"><circle cx="9" cy="9" r="7.5" fill="none" stroke="#86c440" stroke-width="2"/><path d="M5.5 9.2l2.3 2.3 4.7-4.7" fill="none" stroke="#86c440" stroke-width="2"/></svg>Mattress Cleaning &amp; Dust Mites</li>
    <li><svg width="18" height="18" viewBox="0 0 18 18"><circle cx="9" cy="9" r="7.5" fill="none" stroke="#86c440" stroke-width="2"/><path d="M5.5 9.2l2.3 2.3 4.7-4.7" fill="none" stroke="#86c440" stroke-width="2"/></svg>Carpet &amp; Upholstery Cleaning</li>
    <li><svg width="18" height="18" viewBox="0 0 18 18"><circle cx="9" cy="9" r="7.5" fill="none" stroke="#86c440" stroke-width="2"/><path d="M5.5 9.2l2.3 2.3 4.7-4.7" fill="none" stroke="#86c440" stroke-width="2"/></svg>Sub Floor Ventilation</li>
    <li><svg width="18" height="18" viewBox="0 0 18 18"><circle cx="9" cy="9" r="7.5" fill="none" stroke="#86c440" stroke-width="2"/><path d="M5.5 9.2l2.3 2.3 4.7-4.7" fill="none" stroke="#86c440" stroke-width="2"/></svg>Air Conditioning Cleaning</li>
  </ul>

  <div class="tag tag--restore">Restore</div>
  <div class="tag tag--repair">Repair</div>
  <div class="tag tag--maintain">Maintain</div>

  <div class="abs contact-call" style="left:26px; top:764px; font-size:25px; line-height:31px; font-weight:500;">Send a Message<br>or Call our Office</div>
  <div class="abs phone" style="left:15px; top:832px; font-size:27px; gap:8px;">
    <svg width="30" height="30" viewBox="0 0 36 36"><circle cx="18" cy="18" r="16" fill="none" stroke="#86c440" stroke-width="2.5"/><path d="M12 9c1-1 2-1 3 0l2 3c.6 1 .3 2-.5 2.6l-1 .8c1 2.2 2.8 4 5 5l.8-1c.6-.8 1.6-1.1 2.6-.5l3 2c1 1 1 2 0 3l-1.5 1.5c-5 1-14-8-13-13z" fill="#86c440"/></svg>
    0249 55 0183
  </div>
  <div class="abs divider"></div>
  <div class="abs details">
    <div class="row"><svg width="10" height="13" viewBox="0 0 10 13"><path d="M5 0a5 5 0 0 1 5 5c0 3-5 8-5 8S0 8 0 5a5 5 0 0 1 5-5z" fill="#86c440"/><circle cx="5" cy="5" r="1.8" fill="#636466"/></svg><span>PO Box 412, Kellan Vale,<br>NSW. 2390 Australia</span></div>
    <div class="row"><svg width="11" height="9" viewBox="0 0 11 9"><rect width="11" height="9" fill="#86c440"/><path d="M0 0l5.5 5L11 0" fill="none" stroke="#636466" stroke-width="1"/></svg><span>admin@pelmarworkshops.com.au</span></div>
    <div class="row" style="align-items:center;"><svg width="11" height="11" viewBox="0 0 12 12"><circle cx="6" cy="6" r="5.3" fill="none" stroke="#86c440" stroke-width="1.4"/><path d="M0.7 6h10.6M6 0.7c-3 3-3 7.6 0 10.6M6 0.7c3 3 3 7.6 0 10.6" fill="none" stroke="#86c440" stroke-width="1"/></svg><span class="web">www.<span>pelmarworkshops</span>.net</span></div>
  </div>
</section>

</body>
</html>
```